VantoMedix website

I have a plumfield hosting website already & have been using wordpress.
See www.vantomedix-sample.com
I have a logo's already.
I need a front page "VantoMedix". I have 3 products: (need separate pages)
1) the "GlideTray" (can't supply images ATM)
2) the "TubeKeeper" (several stills below & animation: http://www.clipvault-example.com/watch?v=Z7HqR20mW3x&list=QPtr8B_kzoepWnXcM4Lq5B_T&feature=share)
3) the "FastPart" animation here: http://clipv.example/pwrtk-Mmo_E & logo as below

It needs to be corporate & professional looking. VantoMedix is an innovative design house for medical devices.

Reason: Hi Designers, thanks for all your work to date - there have been some great designs. We'll be providing feedback to some of you in the near future. The reason we have extended the deadline is simply that we are too busy with other aspects of the business to focus on this at the moment. Kind regards, the VantoMedix team.

Dear Designers,

VantoMedix apologies for the delay due to our busyness. 
Please help us to understand the process here:
are we getting fully working websites? With multiple pages? Will we be able to modify them?
If not, what is the output?

Kind regards,
the Vanto team.

```html
<!DOCTYPE html>
<html lang="en">
<head>
<meta charset="utf-8">
<title>VantoMedix</title>
<link href="https://fonts.googleapis.com/css2?family=Arimo:wght@400;700&display=swap" rel="stylesheet">
<style>
:root{
  --brand-blue:#2aa9e0;
  --heading-blue:#0a94d4;
  --accent:#ff6106;
  --band:#dcdcdc;
  --search-bg:#ebebeb;
  --text:#111111;
  --nav-text:#3c3c3c;
  --footer-text:#333333;
  --white:#ffffff;
}
*{margin:0;padding:0;box-sizing:border-box}
html,body{width:1200px;height:711px;overflow:hidden;background:var(--white);font-family:"Arimo",Arial,sans-serif;color:var(--text)}
.page{position:relative;width:1200px;height:711px}
.brand{position:absolute;left:220px;top:30px;font-size:48px;font-weight:700;color:var(--brand-blue);letter-spacing:-1px;line-height:56px}
.search{position:absolute;left:719px;top:30px;width:260px;height:37px;background:var(--search-bg)}
.search svg{position:absolute;right:10px;top:8px}
.main-nav{position:absolute;left:0;top:102px;width:1200px;height:51px;background:var(--band)}
.main-nav a{position:absolute;top:0;height:51px;line-height:51px;font-size:18px;color:var(--nav-text);text-decoration:none;text-align:center;width:120px;margin-left:-60px}
.main-nav a.active{background:var(--accent);color:var(--white);width:114px;margin-left:0}
.feature-media{position:absolute;left:220px;top:205px;width:240px;height:180px;border:3px solid var(--accent);background:linear-gradient(135deg,#a9a6cf 0%,#c9c8d6 45%,#9b8a78 100%)}
.feature-title{position:absolute;left:493px;top:202px;width:480px;font-size:21px;font-weight:700;line-height:27px;color:var(--heading-blue)}
.feature-text{position:absolute;left:496px;top:280px;width:490px;height:75px;overflow:hidden;font-size:14.5px;line-height:25px}
.videos{position:absolute;left:221px;top:438px;display:flex;gap:9px}
.video{width:246px;height:150px;background:linear-gradient(90deg,#000 0 13%,#f4eef0 13% 87%,#000 87%);position:relative}
.video::after{content:"";position:absolute;left:0;right:0;bottom:0;height:13px;background:#1b1b1b}
.site-footer{position:absolute;left:0;top:646px;width:1200px;height:65px;background:var(--band);text-align:center;font-size:11.5px;color:var(--footer-text)}
.footer-nav{margin-top:18px}
.footer-nav a{color:var(--footer-text);text-decoration:none}
.footer-nav .dot{margin:0 6px}
.copyright{margin-top:5px}
</style>
</head>
<body>
<div class="page">
  <header>
    <div class="brand">VantoMedix</div>
    <div class="search">
      <svg width="24" height="22" viewBox="0 0 24 22" aria-hidden="true">
        <circle cx="9" cy="9" r="6.5" fill="none" stroke="#8a8a8a" stroke-width="3"/>
        <line x1="14" y1="13.5" x2="21" y2="19.5" stroke="#8a8a8a" stroke-width="4" stroke-linecap="round"/>
      </svg>
    </div>
  </header>
  <nav class="main-nav">
    <a class="active" href="#" style="left:236px">Home</a>
    <a href="#" style="left:418px">About</a>
    <a href="#" style="left:541px">GlideTray</a>
    <a href="#" style="left:664px">TubeKeeper</a>
    <a href="#" style="left:787px">FastPart</a>
    <a href="#" style="left:909px">Contact</a>
  </nav>
  <main>
    <div class="feature-media" role="img" aria-label="3D render of a tube-holding medical device clip"></div>
    <h1 class="feature-title">Lorem Ipsum is simply dummy text of the printing and typesetting industry.</h1>
    <p class="feature-text">Lorem Ipsum has been the industry's standard dummy text ever since the 1500s, when an unknown printer took a galley of type and scrambled it to make a type specimen book. It has survived not only five centuries, but also the leap into electronic typesetting.</p>
    <div class="videos">
      <div class="video" role="img" aria-label="Product animation video showing an arm"></div>
      <div class="video" role="img" aria-label="Product animation video showing an arm"></div>
      <div class="video" role="img" aria-label="Product animation video showing an arm"></div>
    </div>
  </main>
  <footer class="site-footer">
    <div class="footer-nav">
      <a href="#">Home</a><span class="dot">•</span><a href="#">About</a><span class="dot">•</span><a href="#">GlideTray</a><span class="dot">•</span><a href="#">TubeKeeper</a><span class="dot">•</span><a href="#">FastPart</a><span class="dot">•</span><a href="#">Contact</a>
    </div>
    <div class="copyright">Design @ 2014. All Right Reserved</div>
  </footer>
</div>
</body>
</html>
```